Clear Pine Cleaning Services - New Brochure Design Project

Need a very good and polished Brochure from my Commercial Cleaning Services business. I have attached what I have done in the past. Need to take to the next level . Something that will compliment my website .https://merrik-t.webnestly.com/

Target Market(s)

Business /Schools/Churches/ Just about any non-residential establishment

Requirements
Must have
• Professional / Polished look and feel

```html
<!DOCTYPE html>
<html lang="en">
<head>
<meta charset="utf-8">
<title>Clear Pine Cleaning Services – Trifold Brochure</title>
<link href="https://fonts.googleapis.com/css2?family=Open+Sans:ital,wght@0,400;0,600;0,700;0,800;1,400&display=swap" rel="stylesheet">
<style>
:root{
  --navy:#1d3a78;
  --navy-deep:#162e63;
  --blue:#2a5aa8;
  --sky:#29abe2;
  --green:#8dc63f;
  --green-dark:#6fa82a;
  --paper:#ffffff;
  --ink:#2b2f3a;
  --stage:#e4e4e4;
}
*{box-sizing:border-box;margin:0;padding:0}
html,body{width:1200px;height:2402px;overflow:hidden}
body{background:var(--stage);font-family:"Open Sans",Arial,sans-serif;color:var(--ink);position:relative}
.spread{position:absolute;left:51px;width:1098px;height:850px;display:flex;box-shadow:0 18px 40px rgba(0,0,0,.18)}
.spread--outside{top:200px}
.spread--inside{top:1300px}
.panel{position:relative;width:366px;height:850px;overflow:hidden;background:var(--paper)}
.panel--navy{background:var(--navy);color:#fff}
.photo{position:absolute;display:block}
.wave{position:absolute;left:0;width:366px;display:block}
.brand{font-weight:700;color:var(--navy);font-size:26px;line-height:1.1;display:flex;align-items:center;gap:10px}
.brand-dot{width:34px;height:34px;border-radius:50%;background:var(--sky);flex:none}
.tagline{color:var(--green-dark);font-size:15px;font-style:italic}
.phone-pill{position:absolute;display:flex;align-items:center;justify-content:center;gap:10px;background:var(--green);color:#fff;font-weight:700;font-size:22px;border-radius:26px;height:46px;letter-spacing:.5px}
.phone-pill svg{width:22px;height:22px}
.web{position:absolute;width:100%;text-align:center;font-weight:700;font-size:16px;color:#fff}

/* outside flap */
.services-tab{position:absolute;left:0;top:330px;width:200px;height:30px;background:var(--green);color:#fff;font-weight:700;font-size:14px;padding:6px 0 0 26px;letter-spacing:1px}
.service-list{position:absolute;left:26px;top:385px;right:24px;list-style:none}
.service-list li{display:flex;gap:14px;align-items:flex-start;margin-bottom:26px}
.service-icon{width:40px;height:40px;border-radius:50%;background:var(--sky);flex:none}
.service-list h4{font-size:13px;color:var(--navy);font-weight:800}
.service-list p{font-size:11px;color:#666}

/* back panel */
.back-photo{left:103px;top:40px;width:160px;height:160px;border-radius:50%;border:5px solid #fff;background:linear-gradient(135deg,#cfd9e4,#7a95b5)}
.back-brand{position:absolute;top:230px;width:100%;text-align:center;font-weight:700;font-size:20px;color:#fff}
.back-tag{position:absolute;top:262px;width:100%;text-align:center;color:var(--green);font-size:14px;font-style:italic}
.contact-title{position:absolute;top:320px;width:100%;text-align:center;font-weight:800;font-size:20px;letter-spacing:1px}
.contact-copy{position:absolute;top:358px;left:36px;right:36px;text-align:center;font-size:13.5px;line-height:1.55}
.social{position:absolute;top:700px;width:100%;display:flex;justify-content:center;gap:12px}
.social span{width:26px;height:26px;border-radius:50%;border:2px solid rgba(255,255,255,.7)}

/* cover */
.cover-brand{position:absolute;left:40px;top:56px}
.cover-title{position:absolute;top:636px;left:0;width:100%;text-align:center;font-weight:800;font-size:17px;color:var(--navy);white-space:nowrap;letter-spacing:.2px}
.cover-tag{position:absolute;top:670px;width:100%;text-align:center}

/* inside left */
.priority{position:absolute;top:440px;left:28px;right:28px}
.priority h2{color:var(--green);font-size:19px;font-weight:700;margin-bottom:10px}
.priority p{color:#fff;font-size:12px;line-height:1.45;margin-bottom:9px}
.priority .call{color:var(--sky)}

/* inside middle */
.mid-brand{position:absolute;top:40px;width:100%;justify-content:center}
.mid-tag{position:absolute;top:120px;width:100%;text-align:center;font-size:18px;color:var(--green-dark)}
.intro{position:absolute;top:160px;left:32px;right:32px;font-size:12.5px;line-height:1.5;color:#555}
.offer-list{position:absolute;top:266px;left:44px;list-style:none}
.offer-list li{font-size:15px;color:var(--navy);margin-bottom:6px;display:flex;align-items:center;gap:10px}
.offer-list li::before{content:"";width:8px;height:8px;background:var(--green);border-radius:2px}
.mid-quote{position:absolute;top:640px;width:100%;text-align:center;color:var(--sky);font-size:15px;font-weight:600}
.supply-row{position:absolute;top:690px;width:100%;display:flex;justify-content:center;gap:14px}
.supply-row .photo{position:static;width:100px;height:100px;border-radius:50%;border:4px solid #eaeef3}

/* inside right */
.why{position:absolute;top:36px;left:28px;right:24px}
.why h2{color:var(--green);font-weight:800;font-size:20px;margin-bottom:16px}
.why ul{list-style:none}
.why li{display:flex;gap:10px;align-items:center;font-size:13px;padding:7px 0;border-bottom:1px solid rgba(255,255,255,.18)}
.why li svg{width:16px;height:16px;flex:none}
.stars{position:absolute;top:440px;width:100%;text-align:center;color:#f5c518;font-size:20px;letter-spacing:2px}
.why-copy{position:absolute;top:478px;left:40px;right:40px;text-align:center;font-size:12.5px;line-height:1.5}
</style>
</head>
<body>

<section class="spread spread--outside">
  <div class="panel panel--flap">
    <div class="photo" role="img" aria-label="Cleaners mopping and wiping a bright office floor" style="left:0;top:0;width:366px;height:300px;background:linear-gradient(160deg,#e8edf2,#a9b9c8)"></div>
    <svg class="wave" style="top:250px" height="80" viewBox="0 0 366 80"><path d="M0 50 Q180 0 366 30 L366 80 L0 80Z" fill="#fff"/><path d="M0 50 Q180 0 366 30" stroke="var(--green)" stroke-width="6" fill="none"/></svg>
    <div class="services-tab">SERVICES</div>
    <ul class="service-list">
      <li><span class="service-icon"></span><div><h4>COMMERCIAL</h4><p>Offices, retail stores and lobbies</p></div></li>
      <li><span class="service-icon"></span><div><h4>FACILITY</h4><p>Churches, halls and shared buildings</p></div></li>
      <li><span class="service-icon"></span><div><h4>HEALTHCARE</h4><p>Clinics, dental offices and labs</p></div></li>
      <li><span class="service-icon"></span><div><h4>EDUCATIONAL</h4><p>Schools, daycares and college campuses</p></div></li>
      <li><span class="service-icon"></span><div><h4>INDUSTRIAL</h4><p>Warehouses, plants and loading areas</p></div></li>
    </ul>
  </div>

  <div class="panel panel--navy panel--back">
    <div class="photo back-photo" role="img" aria-label="Cleaner mopping a hallway"></div>
    <div class="back-brand">Clear Pine Cleaning Services</div>
    <div class="back-tag">We Enjoy Doing The Dirty Work</div>
    <h3 class="contact-title">CONTACT US</h3>
    <p class="contact-copy">We are a full service cleaning company that offers a full range of quality cleaning services to fit your needs no matter the size. We offer commercial and residential cleaning services for any size property. We take pride in doing your dirty work.</p>
    <div class="phone-pill" style="left:53px;top:610px;width:260px"><svg viewBox="0 0 24 24"><circle cx="12" cy="12" r="11" fill="none" stroke="#fff" stroke-width="2"/><path d="M8 6l2 0 1 3-1.5 1a7 7 0 0 0 3.5 3.5L14 12l3 1v2a2 2 0 0 1-2 2A9 9 0 0 1 7 8a2 2 0 0 1 1-2z" fill="#fff"/></svg>(555) 014-2290</div>
    <div class="social"><span></span><span></span><span></span><span></span></div>
    <div class="web" style="top:770px">merrik-t.webnestly.com</div>
  </div>

  <div class="panel panel--cover">
    <svg class="wave" style="top:0" height="220" viewBox="0 0 366 220"><path d="M0 160 Q180 240 366 130 L366 220 L0 220Z" fill="var(--navy)"/><path d="M0 175 Q180 250 366 148" stroke="var(--green)" stroke-width="6" fill="none"/></svg>
    <div class="brand cover-brand"><span class="brand-dot"></span>Clear Pine<br>Cleaning Services</div>
    <div class="tagline" style="position:absolute;top:130px;left:84px">We enjoy doing the dirty work</div>
    <div class="photo" role="img" aria-label="Bright modern boardroom with a long table and chairs" style="left:0;top:215px;width:366px;height:370px;background:linear-gradient(180deg,#f2f4f6,#9aa6b2)"></div>
    <svg class="wave" style="top:560px" height="70" viewBox="0 0 366 70"><path d="M0 40 Q180 -10 366 30 L366 70 L0 70Z" fill="#fff"/><path d="M0 40 Q180 -10 366 30" stroke="var(--sky)" stroke-width="5" fill="none"/></svg>
    <h1 class="cover-title">PROFESSIONAL CLEANING SERVICES</h1>
    <div class="tagline cover-tag">"We Enjoy Doing the Dirty Work"</div>
    <div class="phone-pill" style="left:53px;top:730px;width:260px"><svg viewBox="0 0 24 24"><circle cx="12" cy="12" r="11" fill="none" stroke="#fff" stroke-width="2"/><path d="M8 6l2 0 1 3-1.5 1a7 7 0 0 0 3.5 3.5L14 12l3 1v2a2 2 0 0 1-2 2A9 9 0 0 1 7 8a2 2 0 0 1 1-2z" fill="#fff"/></svg>(555) 014-2290</div>
  </div>
</section>

<section class="spread spread--inside">
  <div class="panel panel--navy">
    <div class="photo" role="img" aria-label="Gloved hands wiping a polished conference table" style="left:0;top:0;width:366px;height:400px;background:linear-gradient(150deg,#b8a27c,#4d3f30)"></div>
    <svg class="wave" style="top:362px" height="70" viewBox="0 0 366 70"><path d="M0 30 Q180 80 366 20 L366 70 L0 70Z" fill="var(--navy)"/><path d="M0 30 Q180 80 366 20" stroke="var(--green)" stroke-width="6" fill="none"/></svg>
    <div class="priority">
      <h2>Your Business Is Our #1 Priority</h2>
      <p>A clean, organized environment helps businesses run smoothly. The professional team at Clear Pine Cleaning Services offers great value, exceptional commercial cleaning services and focuses on providing the quality cleaning that your business deserves. Knowing that every office or facility has individual needs, we customize commercial cleaning services for businesses and offices.</p>
      <p>We can accommodate many types of commercial cleaning jobs, and we are fully equipped to handle the special needs of your facility.</p>
      <p class="call">Call Clear Pine Cleaning Services today for a free commercial cleaning quote!</p>
    </div>
    <div class="phone-pill" style="left:53px;top:762px;width:260px"><svg viewBox="0 0 24 24"><circle cx="12" cy="12" r="11" fill="none" stroke="#fff" stroke-width="2"/><path d="M8 6l2 0 1 3-1.5 1a7 7 0 0 0 3.5 3.5L14 12l3 1v2a2 2 0 0 1-2 2A9 9 0 0 1 7 8a2 2 0 0 1 1-2z" fill="#fff"/></svg>(555) 014-2290</div>
    <div class="web" style="top:818px">merrik-t.webnestly.com</div>
  </div>

  <div class="panel">
    <div class="brand mid-brand" style="font-size:20px"><span class="brand-dot"></span>Clear Pine Cleaning Services</div>
    <div class="mid-tag">We Enjoy Doing The Dirty Work</div>
    <p class="intro">Whether you're looking for daily, weekly, bi-weekly or monthly cleaning for commercial properties, Clear Pine Cleaning Services will customize a schedule that works best for your customers and your employees.</p>
    <ul class="offer-list">
      <li>Office Cleaning</li><li>Janitorial Services</li><li>Floor Stripping &amp; Waxing</li><li>Day Porter Services</li><li>Window Cleaning</li><li>Kitchen Cleaning</li><li>Restroom Cleaning</li><li>Construction Clean-up</li><li>Deep Cleaning</li><li>Vacant Buildings</li><li>And more!</li>
    </ul>
    <div class="mid-quote">"We Enjoy Doing the Dirty Work"</div>
    <div class="supply-row">
      <div class="photo" role="img" aria-label="Spray bottle and cleaning cloths" style="background:linear-gradient(135deg,#f3d9e6,#c7a3c6)"></div>
      <div class="photo" role="img" aria-label="Bucket of colorful cleaning supplies" style="background:linear-gradient(135deg,#d8f0c8,#6bb8d8)"></div>
      <div class="photo" role="img" aria-label="Vacuum cleaner on carpet" style="background:linear-gradient(135deg,#e6e6e6,#9a9a9a)"></div>
    </div>
  </div>

  <div class="panel panel--navy">
    <div class="why">
      <h2>WHY CHOOSE US?</h2>
      <ul>
        <li><svg viewBox="0 0 16 16"><circle cx="8" cy="8" r="7" fill="none" stroke="#8dc63f" stroke-width="1.5"/><path d="M4.5 8l2.5 2.5 4.5-5" stroke="#8dc63f" stroke-width="1.8" fill="none"/></svg>Always have a personal point of contact.</li>
        <li><svg viewBox="0 0 16 16"><circle cx="8" cy="8" r="7" fill="none" stroke="#8dc63f" stroke-width="1.5"/><path d="M4.5 8l2.5 2.5 4.5-5" stroke="#8dc63f" stroke-width="1.8" fill="none"/></svg>Full on site service management.</li>
        <li><svg viewBox="0 0 16 16"><circle cx="8" cy="8" r="7" fill="none" stroke="#8dc63f" stroke-width="1.5"/><path d="M4.5 8l2.5 2.5 4.5-5" stroke="#8dc63f" stroke-width="1.8" fill="none"/></svg>Bonded service suited to your requirements.</li>
        <li><svg viewBox="0 0 16 16"><circle cx="8" cy="8" r="7" fill="none" stroke="#8dc63f" stroke-width="1.5"/><path d="M4.5 8l2.5 2.5 4.5-5" stroke="#8dc63f" stroke-width="1.8" fill="none"/></svg>Ethical employees.</li>
        <li><svg viewBox="0 0 16 16"><circle cx="8" cy="8" r="7" fill="none" stroke="#8dc63f" stroke-width="1.5"/><path d="M4.5 8l2.5 2.5 4.5-5" stroke="#8dc63f" stroke-width="1.8" fill="none"/></svg>Over 7+ years of satisfied customers.</li>
        <li><svg viewBox="0 0 16 16"><circle cx="8" cy="8" r="7" fill="none" stroke="#8dc63f" stroke-width="1.5"/><path d="M4.5 8l2.5 2.5 4.5-5" stroke="#8dc63f" stroke-width="1.8" fill="none"/></svg>Free No Obligation Quote.</li>
        <li><svg viewBox="0 0 16 16"><circle cx="8" cy="8" r="7" fill="none" stroke="#8dc63f" stroke-width="1.5"/><path d="M4.5 8l2.5 2.5 4.5-5" stroke="#8dc63f" stroke-width="1.8" fill="none"/></svg>Security Of A Fully Bonded Company.</li>
        <li><svg viewBox="0 0 16 16"><circle cx="8" cy="8" r="7" fill="none" stroke="#8dc63f" stroke-width="1.5"/><path d="M4.5 8l2.5 2.5 4.5-5" stroke="#8dc63f" stroke-width="1.8" fill="none"/></svg>100% Satisfaction Guarantee On All Service.</li>
        <li><svg viewBox="0 0 16 16"><circle cx="8" cy="8" r="7" fill="none" stroke="#8dc63f" stroke-width="1.5"/><path d="M4.5 8l2.5 2.5 4.5-5" stroke="#8dc63f" stroke-width="1.8" fill="none"/></svg>A Fully Insured Company.</li>
      </ul>
    </div>
    <div class="stars">★★★★★</div>
    <p class="why-copy">Clear Pine Cleaning Services keeps offices and facilities spotless with careful crews, fair pricing and dependable service every visit.</p>
    <div class="photo" role="img" aria-label="Cleaner mopping a glossy floor beside a wet floor sign" style="left:0;top:610px;width:366px;height:240px;background:linear-gradient(160deg,#c9d3dc,#5f6f7d)"></div>
    <svg class="wave" style="top:590px" height="60" viewBox="0 0 366 60"><path d="M0 0 L366 0 L366 20 Q180 70 0 25Z" fill="var(--navy)"/><path d="M0 25 Q180 70 366 20" stroke="var(--green)" stroke-width="6" fill="none"/></svg>
  </div>
</section>

</body>
</html>
```